Business Card Design For Office Furniture Clearance Company

Kestrel Office Clearance - our company name pretty much explains what we do, we clear offices for high end clients, mainly plc's and large international companies.

We require a nice looking business card that displays professionalism but without being too serious.

It would be nice to see just a little more than a conventional boring business card, make sure you add some flare.

Industry/Entity Type

Office Furniture

Contact Information for Business Card

CARD 1

Tom Pardew
Director
tom@kestrelofficeclearance.co.uk
m: 07700 513928

t: 01632 419063
www.kestrelofficeclearance.co.uk

Kestrel Office Clearance
Unit K4 B
3-7 Ferndale Lane
Harlow Vale
Dunmere
ZZ9 4QX

Clear desks, clear minds… we handle the heavy lifting.

CARD 2

Henry Walbrook
Director
henry@kestrelofficeclearance.co.uk
m: 07700 628157

t: 01632 419063

Kestrel Office Clearance
Unit K4 B
3-7 Ferndale Lane
Harlow Vale
Dunmere
ZZ9 4QX

Font styles to use
Sans Serif

Requirements
Must have
• A white background - as we have a blue logo.
Nice to have
• Nice use of the logo - play around with this and dissect it.

```html
<!DOCTYPE html>
<html lang="en">
<head>
<meta charset="utf-8">
<title>Kestrel Office Clearance – Business Card</title>
<link rel="stylesheet" href="https://fonts.googleapis.com/css2?family=Source+Sans+3:ital,wght@0,400;0,600;1,400&display=swap">
<style>
  :root {
    --page: #8e9092;
    --card-white: #f1f1f3;
    --brand-blue: #1466a6;
    --brand-blue-deep: #0f66a7;
    --ink: #3e3e42;
    --paper: #eeeeef;
  }
  * { box-sizing: border-box; margin: 0; padding: 0; }
  html, body {
    width: 1105px; height: 1200px; overflow: hidden;
    background: var(--page);
    font-family: "Source Sans 3", sans-serif;
  }
  .card { position: absolute; left: 182px; width: 748px; height: 425px; }
  .card--front { top: 119px; background: var(--card-white); color: var(--ink); }
  .card--back { top: 637px; background: var(--brand-blue-deep); }

  .person { position: absolute; left: 45px; top: 46px; }
  .person__name { font-size: 28px; font-weight: 600; color: var(--brand-blue); letter-spacing: .3px; line-height: 1; }
  .person__role { font-size: 20px; margin-top: 6px; line-height: 1; }
  .person__email { font-size: 19px; font-style: italic; margin-top: 8px; line-height: 1; }

  .rule { position: absolute; left: 45px; width: 305px; border-top: 2px dotted var(--brand-blue); }
  .rule--upper { top: 144px; }
  .rule--lower { top: 285px; }

  .address { position: absolute; left: 45px; top: 166px; font-size: 20px; line-height: 26px; font-style: normal; }
  .address__company { font-weight: 600; color: var(--brand-blue); }

  .contacts { position: absolute; left: 45px; top: 302px; list-style: none; font-size: 20px; line-height: 29px; }
  .contacts li { display: flex; align-items: center; gap: 8px; }
  .contacts svg { width: 17px; height: 17px; fill: var(--brand-blue); flex: none; }

  .brand {
    position: absolute; border-radius: 50%;
    display: flex; align-items: center; justify-content: center; text-align: center;
    font-size: 24px; font-weight: 600; line-height: 1.2;
  }
  .brand--front {
    left: 441px; top: 104px; width: 216px; height: 216px;
    background: var(--brand-blue); color: var(--card-white);
  }
  .brand--back {
    left: 258px; top: 81px; width: 230px; height: 230px;
    background: var(--paper); color: var(--brand-blue-deep);
  }

  .tagline {
    position: absolute; left: 0; right: 0; top: 345px; text-align: center;
    font-size: 20px; font-style: italic; color: var(--paper);
  }
</style>
</head>
<body>
  <section class="card card--front">
    <div class="person">
      <p class="person__name">TOM PARDEW</p>
      <p class="person__role">DIRECTOR</p>
      <p class="person__email">tom@kestrelofficeclearance.co.uk</p>
    </div>
    <div class="rule rule--upper"></div>
    <address class="address">
      <span class="address__company">Kestrel Office Clearance</span><br>
      Unit K4 B, 3-7 Ferndale Lane<br>
      Harlow Vale, Dunmere<br>
      ZZ9 4QX
    </address>
    <div class="rule rule--lower"></div>
    <ul class="contacts">
      <li><svg viewBox="0 0 24 24" aria-hidden="true"><path d="M6.6 10.8a15.1 15.1 0 0 0 6.6 6.6l2.2-2.2c.3-.3.7-.4 1-.2 1.1.4 2.3.6 3.6.6.6 0 1 .4 1 1V20c0 .6-.4 1-1 1A17 17 0 0 1 3 4c0-.6.4-1 1-1h3.5c.6 0 1 .4 1 1 0 1.3.2 2.5.6 3.6.1.3 0 .7-.2 1z"/></svg>01632 419063</li>
      <li><svg viewBox="0 0 24 24" aria-hidden="true"><path d="M7 1h10a2 2 0 0 1 2 2v18a2 2 0 0 1-2 2H7a2 2 0 0 1-2-2V3a2 2 0 0 1 2-2zm0 3v14h10V4zm5 15.5a1.2 1.2 0 1 0 0 2.4 1.2 1.2 0 0 0 0-2.4z"/></svg>07700 513928</li>
      <li><svg viewBox="0 0 24 24" aria-hidden="true"><circle cx="12" cy="12" r="10"/><path d="M7 7c2 0 3 1 3 3s2 2 2 4-1 3-1 5M15 4c0 2 1 3 3 3s2 2 3 3" stroke="#f1f1f3" stroke-width="1.6" fill="none"/></svg>www.kestrelofficeclearance.co.uk</li>
    </ul>
    <p class="brand brand--front">Kestrel<br>Office Clearance</p>
  </section>

  <section class="card card--back">
    <p class="brand brand--back">Kestrel<br>Office Clearance</p>
    <p class="tagline">Clear desks, clear minds… we handle the heavy lifting.</p>
  </section>
</body>
</html>
```